Personal Injury Lawyer Billboard

I would like a design created featuring the image of the lawyer centered in the middle of the design.
To the left of the lawyer's image it should read "INJURED?"
To the right of the lawyer's image, it should read "CALL BRUNO!"
Under Call Bruno, include the phone number 318-555-0187.
At the bottom of the design include the lawyers information "Bruno Pemberly Accident & Injury Lawyers"
PLEASE REMOVED THE BACKGROUND IMAGERY OF THE PHOTO SUBMITTED. Also, the colors for this design should match the colors shown in the logo (navy, white and relective soft gold). Please use those color combinations in ways that best stand out.

```html
<!DOCTYPE html>
<html lang="en">
<head>
<meta charset="utf-8">
<title>Bruno Pemberly Accident &amp; Injury Lawyers – Billboard</title>
<link rel="stylesheet" href="https://fonts.googleapis.com/css2?family=Playfair+Display:wght@500;700;800;900&display=swap">
<style>
  :root {
    --navy: #0c1f52;
    --navy-deep: #08163d;
    --navy-ink: #0b1a3f;
    --gold: #b48a2c;
    --gold-soft: #c29a3a;
    --white: #ffffff;
    --serif: "Playfair Display", "Times New Roman", serif;
  }
  html, body {
    margin: 0;
    padding: 0;
    width: 1200px;
    height: 600px;
    overflow: hidden;
    background: var(--white);
  }
  .billboard {
    position: relative;
    width: 1200px;
    height: 600px;
    overflow: hidden;
    font-family: var(--serif);
    background: var(--navy);
  }
  .backdrop {
    position: absolute;
    inset: 0;
  }
  .lawyer-portrait {
    position: absolute;
    left: 405px;
    top: 8px;
    width: 388px;
    height: 516px;
    border-radius: 150px 150px 0 0;
    background: linear-gradient(180deg, #8a6a55 0%, #6d5546 22%, #1c2a5a 40%, #14224d 100%);
  }
  .brand-mark {
    position: absolute;
    left: 52px;
    top: 40px;
    padding: 4px 3px 6px;
    background: var(--navy-deep);
    color: var(--white);
    text-align: center;
  }
  .brand-mark__name {
    display: block;
    font-weight: 700;
    font-size: 30px;
    line-height: 1.05;
    letter-spacing: -0.5px;
    border-bottom: 1.5px solid var(--gold);
    padding-bottom: 4px;
  }
  .brand-mark__practice {
    display: block;
    font-weight: 500;
    font-size: 13.4px;
    line-height: 1;
    padding: 6px 0 5px;
    border-bottom: 1.5px solid var(--gold);
  }
  .headline-question {
    position: absolute;
    left: 18px;
    top: 226px;
    margin: 0;
    color: var(--white);
    font-weight: 900;
    font-size: 70px;
    letter-spacing: -1px;
    line-height: 1;
  }
  .call-to-action {
    position: absolute;
    left: 830px;
    top: 108px;
    margin: 0;
    color: var(--white);
    font-weight: 900;
    font-size: 74px;
    line-height: 1.02;
    letter-spacing: -1px;
  }
  .phone-line {
    position: absolute;
    left: 832px;
    top: 312px;
    display: flex;
    align-items: center;
    gap: 22px;
    color: var(--gold-soft);
    font-weight: 500;
    font-size: 41px;
    line-height: 1;
  }
  .phone-line__icon {
    width: 34px;
    height: 34px;
    fill: var(--gold-soft);
  }
  .footer-band {
    position: absolute;
    left: 0;
    top: 524px;
    width: 1200px;
    height: 76px;
    background: var(--white);
    border-top: 3px solid var(--gold);
    box-sizing: border-box;
  }
  .footer-band__name,
  .footer-band__practice {
    position: absolute;
    top: 8px;
    font-weight: 800;
    font-size: 44px;
    line-height: 1.2;
    letter-spacing: -0.8px;
    white-space: nowrap;
  }
  .footer-band__name {
    left: 38px;
    color: var(--navy-ink);
  }
  .footer-band__practice {
    left: 452px;
    color: var(--gold);
  }
</style>
</head>
<body>
<main class="billboard">
  <svg class="backdrop" width="1200" height="600" viewBox="0 0 1200 600" aria-hidden="true">
    <defs>
      <linearGradient id="panel-left" x1="0" y1="0" x2="1" y2="1">
        <stop offset="0" stop-color="#0a1c55"/>
        <stop offset="1" stop-color="#0f2a6a"/>
      </linearGradient>
      <linearGradient id="panel-right" x1="0" y1="0" x2="1" y2="1">
        <stop offset="0" stop-color="#0b1d4e"/>
        <stop offset="1" stop-color="#0d2156"/>
      </linearGradient>
    </defs>
    <rect class="panel-left" x="0" y="0" width="500" height="524" fill="url(#panel-left)"/>
    <rect class="panel-right" x="740" y="0" width="460" height="524" fill="url(#panel-right)"/>
    <polygon class="corner-accent" points="0,0 66,0 0,91" fill="#b48a2c"/>
    <polygon class="gold-band" points="498,0 812,0 746,524 344,524" fill="#b48a2c"/>
    <polygon class="divider-left" points="487,0 496,0 346,524 337,524" fill="#ffffff"/>
    <polygon class="divider-right" points="814,0 823,0 755,524 746,524" fill="#ffffff"/>
  </svg>

  <div class="lawyer-portrait" role="img" aria-label="Cut-out photo of the lawyer in a navy suit, white shirt and green tie, smiling with a raised fist"></div>

  <div class="brand-mark">
    <span class="brand-mark__name">BRUNO PEMBERLY</span>
    <span class="brand-mark__practice">ACCIDENT &amp; INJURY LAWYERS</span>
  </div>

  <h1 class="headline-question">INJURED?</h1>

  <h2 class="call-to-action">CALL<br>BRUNO!</h2>

  <div class="phone-line">
    <svg class="phone-line__icon" viewBox="0 0 24 24" aria-hidden="true">
      <path d="M6.6 10.8c1.4 2.8 3.8 5.1 6.6 6.6l2.2-2.2c.3-.3.7-.4 1-.2 1.1.4 2.3.6 3.6.6.6 0 1 .4 1 1V20c0 .6-.4 1-1 1C10.6 21 3 13.4 3 4c0-.6.4-1 1-1h3.5c.6 0 1 .4 1 1 0 1.3.2 2.5.6 3.6.1.3 0 .7-.2 1L6.6 10.8z"/>
    </svg>
    <span class="phone-line__number">318-555-0187</span>
  </div>

  <footer class="footer-band">
    <span class="footer-band__name">BRUNO PEMBERLY</span>
    <span class="footer-band__practice">ACCIDENT &amp; INJURY LAWYERS</span>
  </footer>
</main>
</body>
</html>
```